Bref créative
Stationary for KORVEL Trademark & Licensing
KORVEL Trademark & Licensing
Professional
Piet Morrow
VP of Technology
437 E. Alder Rd.
Duncan, OK 73408
Piet.Morrow@korvelmarks.example
www.korvelmarks.example
Our website is not up yet, so please do not try to use this for a sample.
Our business is to trademark and licensing school logos and products. We are looking for a very professional & clean product.
I am looking for some ideas for the back our slogan "Making Your Logo Work for You" should be there somewhere.
Company Logo for KORVEL Trademark & Licensing

```html
<!DOCTYPE html>
<html lang="en">
<head>
<meta charset="utf-8">
<title>KORVEL Trademark &amp; Licensing – Business Card</title>
<link rel="stylesheet" href="https://fonts.googleapis.com/css2?family=Tinos:wght@400;700&display=swap">
<style>
  :root {
    --page-bg: #e9e6e1;
    --card-bg: #ffffff;
    --brand-blue: #1f5fb5;
    --deep-blue: #0b3f8f;
    --sky-blue: #3f8fe0;
    --ink: #2f2f33;
    --silver: #b9bec6;
  }
  * { margin: 0; padding: 0; box-sizing: border-box; }
  html, body {
    width: 1200px; height: 965px; overflow: hidden;
    background: var(--page-bg);
    font-family: "Tinos", "Times New Roman", serif;
  }
  .business-card {
    position: absolute; left: 100px; top: 197px;
    width: 1000px; height: 571px;
    background: var(--card-bg);
    border-radius: 30px;
    overflow: hidden;
    box-shadow: 0 14px 36px rgba(0,0,0,.18);
  }
  .card-swoosh { position: absolute; inset: 0; width: 100%; height: 100%; }
  .brand-mark {
    position: absolute; left: 70px; top: 80px; width: 340px;
    text-align: center;
  }
  .brand-circle {
    width: 240px; height: 240px; margin: 0 auto 18px;
    border-radius: 50%;
    background: radial-gradient(circle at 45% 40%, var(--sky-blue), var(--deep-blue));
  }
  .brand-name {
    color: var(--brand-blue); font-weight: 700;
    font-size: 26px; line-height: 1.2; letter-spacing: .5px;
  }
  .contact-block { position: absolute; left: 450px; top: 55px; color: var(--ink); }
  .person-name { color: var(--brand-blue); font-weight: 700; font-size: 46px; line-height: 1; }
  .person-title { color: var(--brand-blue); font-size: 27px; margin-top: 6px; }
  .address { margin-top: 36px; font-size: 27px; line-height: 1.25; }
  .contact-list { list-style: none; margin-top: 18px; font-size: 26px; }
  .contact-list li { display: flex; align-items: center; height: 38px; }
  .contact-list svg { width: 24px; height: 24px; margin-right: 14px; fill: var(--brand-blue); flex: none; }
</style>
</head>
<body>
  <article class="business-card">
    <svg class="card-swoosh" viewBox="0 0 1000 571" preserveAspectRatio="none" aria-hidden="true">
      <defs>
        <linearGradient id="swooshBlue" x1="0" y1="0" x2="1" y2="0">
          <stop offset="0" stop-color="#0b3f8f"/>
          <stop offset=".55" stop-color="#2a78d4"/>
          <stop offset="1" stop-color="#1550a8"/>
        </linearGradient>
      </defs>
      <path d="M0,550 C300,530 640,478 1000,468" fill="none" stroke="var(--silver)" stroke-width="9"/>
      <path d="M0,571 C300,558 660,500 1000,490 L1000,571 Z" fill="url(#swooshBlue)"/>
      <path d="M0,571 C320,560 670,512 1000,505" fill="none" stroke="#8cc2f5" stroke-width="3" opacity=".7"/>
    </svg>

    <div class="brand-mark">
      <div class="brand-circle"></div>
      <p class="brand-name">KORVEL<br>Trademark &amp; Licensing</p>
    </div>

    <div class="contact-block">
      <h1 class="person-name">Piet Morrow</h1>
      <p class="person-title">VP of Technology</p>
      <p class="address">437 E. Alder Rd.<br>Duncan, OK 73408</p>
      <ul class="contact-list">
        <li><svg viewBox="0 0 24 24"><path d="M6.6 10.8a15 15 0 0 0 6.6 6.6l2.2-2.2a1 1 0 0 1 1-.25 11.4 11.4 0 0 0 3.6.57 1 1 0 0 1 1 1V20a1 1 0 0 1-1 1A17 17 0 0 1 3 4a1 1 0 0 1 1-1h3.5a1 1 0 0 1 1 1c0 1.25.2 2.45.57 3.6a1 1 0 0 1-.25 1z"/></svg>555-301-4682</li>
        <li><svg viewBox="0 0 24 24"><path d="M7 1h10a2 2 0 0 1 2 2v18a2 2 0 0 1-2 2H7a2 2 0 0 1-2-2V3a2 2 0 0 1 2-2zm0 3v14h10V4zm5 15.5a1.2 1.2 0 1 0 0 2.4 1.2 1.2 0 0 0 0-2.4z"/></svg>555-017-9354</li>
        <li><svg viewBox="0 0 24 24"><path d="M12 2a10 10 0 1 0 5 18.7l-1-1.7A8 8 0 1 1 20 12v1.5a1.5 1.5 0 0 1-3 0V7h-2v1a5 5 0 1 0 .7 7.2A3.5 3.5 0 0 0 22 13.5V12A10 10 0 0 0 12 2zm0 13a3 3 0 1 1 0-6 3 3 0 0 1 0 6z"/></svg>Piet.Morrow@korvelmarks.example</li>
        <li><svg viewBox="0 0 24 24"><path d="M12 2a10 10 0 1 0 0 20 10 10 0 0 0 0-20zm6.9 6h-3a15 15 0 0 0-1.4-3.9A8 8 0 0 1 18.9 8zM12 4a13 13 0 0 1 1.9 4h-3.8A13 13 0 0 1 12 4zM4.3 14a8 8 0 0 1 0-4h3.4a16 16 0 0 0 0 4zm.8 2h3a15 15 0 0 0 1.4 3.9A8 8 0 0 1 5.1 16zm3-8h-3a8 8 0 0 1 4.4-3.9A15 15 0 0 0 8.1 8zM12 20a13 13 0 0 1-1.9-4h3.8A13 13 0 0 1 12 20zm2.3-6H9.7a14 14 0 0 1 0-4h4.6a14 14 0 0 1 0 4zm.2 5.9a15 15 0 0 0 1.4-3.9h3a8 8 0 0 1-4.4 3.9zM16.3 14a16 16 0 0 0 0-4h3.4a8 8 0 0 1 0 4z"/></svg>www.korvelmarks.example</li>
      </ul>
    </div>
  </article>
</body>
</html>
```